Stationery Design Project

KT7 Staffing requires letterhead and business card designs for a company based in London. Just like the name, we're a management resourcing company, providing resources to third party companies. You can see www.kt7staffing-example.com for ideas on existing colour schemes and design concepts that have been implimented and agreed to. Ultimately the design should broadcast professionalism, safety and the concept of growth.

Target Market(s)

Financial institutes; friendly societies (All UK based)

Industry/Entity Type

Safety

Requirements
Must have
• Files produced should be print ready; and the text in them editable (eg address, name etc)

```html
<!DOCTYPE html>
<html lang="en">
<head>
<meta charset="utf-8">
<title>KT7 Staffing — Stationery</title>
<link rel="stylesheet" href="https://fonts.googleapis.com/css2?family=Arimo:ital,wght@0,400;0,700;1,700&display=swap">
<style>
  :root {
    --bg-top: #f4f8fa;
    --bg-bottom: #cfe3ea;
    --paper: #ffffff;
    --teal: #1f9aa8;
    --teal-dark: #178a98;
    --teal-light: #8fd0d9;
    --teal-pale: #7fc3cf;
    --ink-grey: #7a7a7a;
    --white: #ffffff;
    --shadow: rgba(30, 70, 85, 0.28);
  }
  * { box-sizing: border-box; margin: 0; padding: 0; }
  html, body { width: 1200px; height: 627px; overflow: hidden; }
  body {
    font-family: "Arimo", Arial, sans-serif;
    background: linear-gradient(160deg, var(--bg-top) 0%, var(--bg-bottom) 100%);
    position: relative;
  }

  /* Letterhead */
  .letterhead {
    position: absolute; left: 99px; top: 34px;
    width: 375px; height: 557px;
    background: var(--paper);
    box-shadow: 0 2px 8px var(--shadow);
    overflow: hidden;
  }
  .brand {
    display: flex; align-items: center; gap: 6px;
    color: var(--teal); font-weight: 700; white-space: nowrap;
  }
  .brand-dot { border-radius: 50%; background: var(--teal); flex: none; }
  .letterhead .brand { position: absolute; left: 26px; top: 22px; font-size: 12px; }
  .letterhead .brand-dot { width: 10px; height: 10px; }
  .letterhead-wave { position: absolute; left: 0; bottom: 0; width: 100%; height: 100px; }
  .letterhead-footer {
    position: absolute; left: 0; right: 0; bottom: 18px;
    display: flex; justify-content: center; gap: 14px;
    color: var(--white); font-size: 10.5px; line-height: 14px;
  }
  .footer-address { text-align: right; padding-left: 60px; }
  .footer-address .company { font-weight: 700; }
  .footer-divider { width: 1px; background: rgba(255,255,255,0.8); }
  .footer-contact { font-weight: 700; }

  /* Business card */
  .card {
    position: absolute; width: 300px; height: 430px;
    box-shadow: 0 4px 12px var(--shadow);
    overflow: hidden;
  }
  .card-front { left: 540px; top: 80px; background: var(--paper); }
  .card-front .brand { position: absolute; left: 30px; top: 40px; font-size: 24px; }
  .card-front .brand-dot { width: 18px; height: 18px; }
  .card-person { position: absolute; left: 72px; top: 160px; }
  .person-name { color: var(--teal); font-size: 15px; text-transform: uppercase; }
  .person-role { color: var(--teal-pale); font-size: 12px; margin-top: 2px; }
  .card-details { position: absolute; left: 86px; top: 225px; color: var(--ink-grey); font-size: 11.5px; line-height: 15px; }
  .card-email { display: block; margin-top: 16px; color: var(--teal); text-decoration: underline; }
  .card-phones { display: grid; grid-template-columns: 38px auto; margin-top: 16px; }
  .card-phones dt { font-weight: 700; }
  .card-wave { position: absolute; left: 0; bottom: 0; width: 100%; height: 110px; }
  .card-web {
    position: absolute; left: 60px; bottom: 22px;
    color: rgba(255,255,255,0.85); font-size: 12px; font-weight: 700; font-style: italic;
  }

  .card-back {
    left: 870px; top: 110px;
    background: linear-gradient(200deg, var(--teal-light) 0%, var(--teal) 55%, var(--teal-dark) 100%);
  }
  .card-back .brand {
    position: absolute; left: 0; right: 0; top: 190px; justify-content: center;
    color: rgba(255,255,255,0.35); font-size: 26px;
  }
  .card-back .brand-dot { width: 18px; height: 18px; background: rgba(255,255,255,0.35); }
</style>
</head>
<body>

<section class="letterhead" aria-label="Letterhead">
  <div class="brand"><span class="brand-dot"></span>KT7 Staffing</div>
  <svg class="letterhead-wave" viewBox="0 0 375 100" preserveAspectRatio="none" aria-hidden="true">
    <defs>
      <linearGradient id="lhWave" x1="0" x2="1" y1="0" y2="0">
        <stop offset="0" stop-color="var(--teal-dark)"/>
        <stop offset="1" stop-color="var(--teal-light)"/>
      </linearGradient>
    </defs>
    <path d="M0 45 C 60 5, 140 0, 220 20 C 290 38, 340 42, 375 32 L375 100 L0 100 Z" fill="url(#lhWave)"/>
  </svg>
  <footer class="letterhead-footer">
    <div class="footer-address">
      <div class="company">KT7 Staffing,</div>
      <div>14 Alder Court,</div>
      <div>London, N4 2QX</div>
    </div>
    <div class="footer-divider"></div>
    <div class="footer-contact">
      <div>+44 (0) 20 7946 0123</div>
      <div>+44 (0) 7700 900 456</div>
      <div>www.kt7staffing-example.com</div>
    </div>
  </footer>
</section>

<section class="card card-front" aria-label="Business card front">
  <div class="brand"><span class="brand-dot"></span>KT7 Staffing</div>
  <div class="card-person">
    <div class="person-name">Harriet Caldwell</div>
    <div class="person-role">Graphic Designer</div>
  </div>
  <div class="card-details">
    <div>14 Alder Court, London,<br>N4 2QX</div>
    <span class="card-email">harriet.c@example.com</span>
    <dl class="card-phones">
      <dt>Direct</dt><dd>+44 (0) 20 7946 0123</dd>
      <dt>Mob</dt><dd>+44 (0) 7700 900 456</dd>
    </dl>
  </div>
  <svg class="card-wave" viewBox="0 0 300 110" preserveAspectRatio="none" aria-hidden="true">
    <defs>
      <linearGradient id="cardWave" x1="0" x2="1" y1="0" y2="0">
        <stop offset="0" stop-color="var(--teal-dark)"/>
        <stop offset="1" stop-color="var(--teal-light)"/>
      </linearGradient>
    </defs>
    <path d="M0 70 C 40 20, 110 10, 180 18 C 240 25, 275 20, 300 10 L300 110 L0 110 Z" fill="url(#cardWave)"/>
  </svg>
  <div class="card-web">www.kt7staffing-example.com</div>
</section>

<section class="card card-back" aria-label="Business card back">
  <div class="brand"><span class="brand-dot"></span>KT7 Staffing</div>
</section>

</body>
</html>
```